Financial Services business needs banner showcasing past stock picks

We are looking for a banner for our Vancouver B.C. based company named 'BrightHarbor Financial'. Our website is www.tidalpicks-example.com and we provide several stock picking services to clients which we let them know which stocks to buy. We have an impressive track record of picking some of the best stocks on the Canadian and American stock markets and we would like to showcase some of these stocks to prospective clients at conferences.

```html
<!DOCTYPE html>
<html lang="en">
<head>
<meta charset="utf-8">
<title>BrightHarbor Financial – Roll-up Banner</title>
<link href="https://fonts.googleapis.com/css2?family=Arvo:wght@700&family=Bitter:wght@400&family=Montserrat:wght@400;500&display=swap" rel="stylesheet">
<style>
  :root {
    --teal: #24a999;
    --navy: #2d3e4e;
    --ink: #23303c;
    --white: #ffffff;
    --stage: #e4e5e1;
    --chart-line: #c8102e;
    --grid: #e4e4e4;
  }
  * { box-sizing: border-box; margin: 0; padding: 0; }
  html, body { width: 1200px; height: 1200px; overflow: hidden; background: var(--stage); }
  .stage { position: relative; width: 1200px; height: 1200px; overflow: hidden; }
  .banner {
    position: absolute; left: 410px; top: 12px;
    width: 550px; height: 1700px;
    transform: scale(0.6918); transform-origin: top left;
    background: var(--white);
    overflow: hidden;
    box-shadow: 0 6px 30px rgba(0,0,0,.18);
  }
  .banner-shapes { position: absolute; inset: 0; width: 550px; height: 1700px; }
  .brand { position: absolute; top: 200px; left: 0; width: 550px; text-align: center; }
  .brand-name {
    font-family: "Montserrat", sans-serif; font-weight: 400;
    font-size: 40px; color: var(--teal); letter-spacing: 1px;
  }
  .brand-tagline {
    margin-top: 18px;
    font-family: "Montserrat", sans-serif; font-weight: 500;
    font-size: 20px; color: var(--ink); letter-spacing: 3.5px;
  }
  .headline {
    position: absolute; top: 375px; left: 0; width: 550px; text-align: center;
    font-family: "Arvo", serif; font-weight: 700; font-size: 38px;
    color: var(--teal); letter-spacing: -1px;
  }
  .intro {
    position: absolute; top: 435px; left: 0; width: 550px; text-align: center;
    font-family: "Bitter", serif; font-size: 25px; line-height: 36px; color: var(--ink);
  }
  .chart-card {
    position: absolute; width: 250px; height: 210px;
    background: var(--white);
    box-shadow: 0 8px 10px rgba(0,0,0,.28);
  }
  .chart-card svg { display: block; width: 100%; height: 100%; }
  .card-a { left: 32px; top: 715px; transform: rotate(-2deg); }
  .card-b { left: 300px; top: 705px; width: 225px; transform: rotate(-2deg); }
  .card-c { left: 180px; top: 950px; width: 235px; height: 215px; transform: rotate(-2deg); }
  .chart-title { font-family: "Montserrat", sans-serif; font-weight: 500; font-size: 7px; fill: var(--ink); }
  .chart-small { font-family: "Montserrat", sans-serif; font-size: 4px; fill: #666; }
  .chart-axis { font-family: "Montserrat", sans-serif; font-size: 4px; fill: var(--chart-line); }
  .chart-source { font-family: "Montserrat", sans-serif; font-weight: 500; font-size: 5px; fill: var(--ink); }
  .slogan {
    position: absolute; top: 1315px; left: 0; width: 550px; text-align: center;
    font-family: "Arvo", serif; font-weight: 700; font-size: 34px; color: var(--teal);
    transform: rotate(-8deg);
  }
  .site-url {
    position: absolute; top: 1560px; left: 40px; width: 480px; text-align: center;
    font-family: "Arvo", serif; font-weight: 700; font-size: 24px; color: var(--white);
    letter-spacing: 1px; transform: rotate(-14deg);
  }
</style>
</head>
<body>
<div class="stage">
  <section class="banner">
    <svg class="banner-shapes" viewBox="0 0 550 1700" aria-hidden="true">
      <polygon points="0,575 215,635 0,705" fill="var(--navy)"/>
      <polygon points="0,705 550,540 550,1105 460,1145 0,1350" fill="var(--teal)"/>
      <polygon points="460,1145 550,1105 550,1160" fill="var(--navy)"/>
      <polygon points="0,1515 215,1515 0,1625" fill="var(--teal)"/>
      <polygon points="550,1345 550,1700 0,1700 0,1625" fill="var(--navy)"/>
    </svg>

    <header class="brand">
      <div class="brand-name">BrightHarbor Financial</div>
      <div class="brand-tagline">INDEPENDENT EQUITY ADVISORS</div>
    </header>

    <h1 class="headline">Research. Results. Freedom.</h1>
    <p class="intro">Building simple, winning stock<br>portfolios to beat the market.</p>

    <figure class="chart-card card-a">
      <svg viewBox="0 0 250 210" preserveAspectRatio="none">
        <text class="chart-title" x="18" y="32">Gold Equity Index in 1997</text>
        <text class="chart-small" x="18" y="40">Daily closes</text>
        <text class="chart-source" x="185" y="34">Dawnline Research</text>
        <rect x="32" y="50" width="200" height="135" fill="#f6f6f6"/>
        <g stroke="var(--grid)" stroke-width=".6">
          <line x1="32" y1="70" x2="232" y2="70"/><line x1="32" y1="95" x2="232" y2="95"/>
          <line x1="32" y1="120" x2="232" y2="120"/><line x1="32" y1="145" x2="232" y2="145"/>
          <line x1="32" y1="170" x2="232" y2="170"/><line x1="70" y1="50" x2="70" y2="185"/>
          <line x1="170" y1="50" x2="170" y2="185"/>
        </g>
        <text class="chart-axis" x="14" y="60">$190</text><text class="chart-axis" x="14" y="120">$140</text><text class="chart-axis" x="14" y="183">$90</text>
        <polyline fill="none" stroke="var(--chart-line)" stroke-width=".9" points="36,100 42,96 48,102 54,95 60,98 66,70 70,66 76,78 82,90 88,98 94,110 100,104 106,114 112,108 118,116 124,112 130,120 136,114 142,118 148,110 154,116 160,124 166,112 172,100 176,108 180,140 186,156 192,168 198,176 204,172 210,180 216,174 222,178"/>
        <g class="chart-small"><text x="34" y="195">Jan</text><text x="70" y="195">Mar</text><text x="106" y="195">May</text><text x="140" y="195">Jul</text><text x="172" y="195">Sep</text><text x="206" y="195">Nov</text></g>
        <text class="chart-small" x="10" y="130" transform="rotate(-90 10 130)">Index level</text>
      </svg>
    </figure>

    <figure class="chart-card card-b">
      <svg viewBox="0 0 250 210" preserveAspectRatio="none">
        <text class="chart-title" x="18" y="32">Gold Equity Index in 1997</text>
        <text class="chart-small" x="18" y="40">Daily closes</text>
        <text class="chart-source" x="185" y="34">Dawnline Research</text>
        <rect x="32" y="50" width="200" height="135" fill="#f6f6f6"/>
        <g stroke="var(--grid)" stroke-width=".6">
          <line x1="32" y1="70" x2="232" y2="70"/><line x1="32" y1="95" x2="232" y2="95"/>
          <line x1="32" y1="120" x2="232" y2="120"/><line x1="32" y1="145" x2="232" y2="145"/>
          <line x1="32" y1="170" x2="232" y2="170"/><line x1="200" y1="50" x2="200" y2="185"/>
        </g>
        <text class="chart-axis" x="14" y="60">$190</text><text class="chart-axis" x="14" y="120">$140</text><text class="chart-axis" x="14" y="183">$90</text>
        <polyline fill="none" stroke="var(--chart-line)" stroke-width=".9" points="36,100 42,96 48,102 54,95 60,98 66,70 70,66 76,78 82,90 88,98 94,110 100,104 106,114 112,108 118,116 124,112 130,120 136,114 142,118 148,110 154,116 160,124 166,112 172,100 176,108 180,140 186,156 192,168 198,176 204,172 210,180 216,174 222,178"/>
        <g class="chart-small"><text x="34" y="195">Jan</text><text x="70" y="195">Mar</text><text x="106" y="195">May</text><text x="140" y="195">Jul</text><text x="172" y="195">Sep</text><text x="206" y="195">Nov</text></g>
      </svg>
    </figure>

    <figure class="chart-card card-c">
      <svg viewBox="0 0 250 210" preserveAspectRatio="none">
        <text class="chart-title" x="18" y="32">Gold Equity Index in 1997</text>
        <text class="chart-small" x="18" y="40">Daily closes</text>
        <text class="chart-source" x="185" y="34">Dawnline Research</text>
        <rect x="32" y="50" width="200" height="135" fill="#f6f6f6"/>
        <g stroke="var(--grid)" stroke-width=".6">
          <line x1="32" y1="70" x2="232" y2="70"/><line x1="32" y1="95" x2="232" y2="95"/>
          <line x1="32" y1="120" x2="232" y2="120"/><line x1="32" y1="145" x2="232" y2="145"/>
          <line x1="32" y1="170" x2="232" y2="170"/><line x1="100" y1="50" x2="100" y2="185"/>
        </g>
        <text class="chart-axis" x="14" y="60">$190</text><text class="chart-axis" x="14" y="120">$140</text><text class="chart-axis" x="14" y="183">$90</text>
        <polyline fill="none" stroke="var(--chart-line)" stroke-width=".9" points="36,100 42,96 48,102 54,95 60,98 66,70 70,66 76,78 82,90 88,98 94,110 100,104 106,114 112,108 118,116 124,112 130,120 136,114 142,118 148,110 154,116 160,124 166,112 172,100 176,108 180,140 186,156 192,168 198,176 204,172 210,180 216,174 222,178"/>
        <g class="chart-small"><text x="34" y="195">Jan</text><text x="70" y="195">Mar</text><text x="106" y="195">May</text><text x="140" y="195">Jul</text><text x="172" y="195">Sep</text><text x="206" y="195">Nov</text></g>
      </svg>
    </figure>

    <p class="slogan">Investing Done Differently</p>
    <p class="site-url">www.tidalpicks-example.com</p>
  </section>
</div>
</body>
</html>
```